ROSE WINE LABEL

WE NEED A LABEL DESIGN FOR A NEW ROSE WINE MADE IN MEXICO. THIS IS A NEW WINARY THAT WANTS TO DO SOMETHING DIFFERENT FOR THE WINE INDUSTRY IN MEXICO, EXCELENT QUALITY OF WINE ACCESIBLE FOR EVERYONE. WINE CULTURE IN MEXICO IS NOT GOOD, WE WANT TO INNOVATE IN THE MARKET, BRING WINE TO YOUNG PEOPLE WITHOUT MAKING IT SEAM LIKE A "LUXURY" PRODUCT, LET THEM KNOW THAT YOU CAN DRINK WINE EVERYDAY EVERYTIME, SOMETHING EASY TO ANALYZE, DRINK AND UNDERSTAND, SOMETHING TO LET KNOW THE CONSUMERS ABOUT THE GOOD QUALITY OF WINE YOU CAN FIND IN MEXICO. I WANT TO SEE A DIFFERENT DESIGN. WE WANT TO KEEP WORKING WITH THE DESIGNER FOR THE REST OF THE LABELS, AROUND 6-7. THE NAME OF THE WINARY IS "VINOS DEL ROBLEDAL" AND THE NAMES OF THE WINES ARE GOING TO HAVE THE "ROBLEDAL" AND THE DIFFERENT FINE ARTS LIKE PAINTING, DANCE, LITERATURE, ETC.
THE BOTTLE OF THIS WINE IS GOING TO BE REGULAR SHAPE ALSO KNOWN AS BODEAUX, TRANSPARENT AND LIGHT GREEN ALSO KNOWN AS "GREEN CHAMPAGNE", SILVER & BLACK CAPSULE.

Requirements
Must have
• THE LABEL MUST HAVE THE NAME OF THE WINE "BAILE DE LA ROBLEDANA" AND IN A SMALLER FONT "QUERÉTARO, MÉXICO"
Nice to have
• A COLORFUL AND MODERN DESIGN, I AM ATTACHING THE LOGO OF THE WINARY. IT IS NOT NECESARY TO ADD IT TO THE LABEL, BUT PERHAPS SOMEONE IS INTERESTED IN THE "VR" OF THE DESIGN FROM INSIDE THE SHELL.
Should not have
• THE DESIGN SHOULD BE ABLE TO FIT IN A REGULAR FORM, RECTANGULAR, SQUARE, OR CIRCLE, NO SPECIAL DIE CUTTING CAN BE MADE TO THE LABEL.

```html
<!DOCTYPE html>
<html lang="es">
<head>
<meta charset="utf-8">
<title>Baile de la Robledana · Etiqueta</title>
<link rel="stylesheet" href="https://fonts.googleapis.com/css2?family=Antonio:wght@100;300&display=swap">
<style>
  :root {
    --backdrop: #ececec;
    --weave-violet: #4a2a86;
    --magenta: #ec008c;
    --yellow: #fff200;
    --teal: #2bbb9e;
    --orange: #f7861f;
    --sky: #00aeef;
    --band: #062806;
    --ink-light: #f4f4f4;
  }
  html, body {
    margin: 0;
    width: 1200px;
    height: 1000px;
    overflow: hidden;
    background: var(--backdrop);
  }
  .canvas {
    width: 1200px;
    height: 1000px;
    display: flex;
    align-items: center;
    justify-content: center;
  }
  .wine-label {
    width: 473px;
    height: 943px;
    display: block;
    box-shadow: 0 2px 10px rgba(0,0,0,0.12);
  }
  .wine-name {
    font-family: "Antonio", "Arial Narrow", sans-serif;
    font-weight: 100;
    fill: var(--ink-light);
  }
  .wine-origin, .wine-abv {
    font-family: "Antonio", "Arial Narrow", sans-serif;
    font-weight: 300;
    fill: var(--ink-light);
  }
</style>
</head>
<body>
<main class="canvas">
  <svg class="wine-label" viewBox="0 0 394 786" xmlns="http://www.w3.org/2000/svg" aria-labelledby="label-title">
    <title id="label-title">Baile de la Robledana — Querétaro, México</title>

    <rect class="weave-field" x="0" y="0" width="394" height="786" fill="var(--weave-violet)"
          role="img" aria-label="Woven zigzag pattern in magenta, violet and navy"/>

    <g class="dot-scatter">
      <circle class="dot dot-magenta" cx="128" cy="148" r="108" fill="var(--magenta)"/>
      <circle class="dot dot-teal" cx="332" cy="72" r="38" fill="var(--teal)"/>
      <circle class="dot dot-yellow" cx="304" cy="226" r="66" fill="var(--yellow)"/>
      <circle class="dot dot-orange" cx="104" cy="566" r="62" fill="var(--orange)"/>
      <circle class="dot dot-sky" cx="302" cy="648" r="36" fill="var(--sky)"/>
    </g>

    <rect class="name-band" x="0" y="319" width="394" height="115" fill="var(--band)"/>

    <text class="wine-name" x="366" y="378" text-anchor="end" font-size="58"
          textLength="342" lengthAdjust="spacingAndGlyphs">BAILE DE LA ROBLEDANA</text>
    <text class="wine-origin" x="365" y="407" text-anchor="end" font-size="15"
          textLength="118" lengthAdjust="spacingAndGlyphs">QUERÉTARO, MÉXICO</text>

    <text class="wine-abv" x="365" y="770" text-anchor="end" font-size="13"
          textLength="53" lengthAdjust="spacingAndGlyphs">ALC 12.5%</text>
  </svg>
</main>
</body>
</html>
```